Amazing Website for innovative Tax-App

Background:
Our Company "Rendolo" provides all employees an App, that allows them to file their tax easy, in only a few minutes and most importantly without any prior knowledge. Most people miss out on their well deserved tax refund. Rendolo helps these people to not only get back their money, but also to maximise their refund.
Task:
Please help us create a beautiful and high quality Webdesign with breathtaking mockups, which immediately reflects what rendolo stands for.
Rendolo is THE tool for getting back tax money (could have a slightly official government touch)
Rendolo breaks down complex old procedures in the utmost easiest way, so that filing your tax via app with a few clicks becomes almost fun.
Additional:
Please surprise us with great mockups, that showcases our app, maybe some icons that reflects users individual life and flying around. (Taxes are as individual as users life!
Maybe catch people with a notification that shows that in your online banking you got around 1000€ in refund and create excitement that "you could be the next"
Work with the newest iphone devices as mockup and use screenshots that are provided in files. You can also think of creating some 3D elements around the phone.
this is how our current website looks like: www.rendolo-beispiel.at
You can take inspirations from that existing site.
Plus, this is is a website from another company in the same field that we like: https://www.kassmiro-beispiel.com/
Please provide complete desktop and mobile website Design and most importantly..
Please be creative!

```html
<!DOCTYPE html>
<html lang="en">
<head>
<meta charset="utf-8">
<title>Rendolo – Get back your tax money</title>
<link href="https://fonts.googleapis.com/css2?family=Poppins:wght@400;500;600;700&display=swap" rel="stylesheet">
<style>
  :root{
    --teal:#14c0a8;
    --ink:#2b2b2b;
    --text:#3a3a3a;
    --muted:#666;
    --hero-bg:#f1f2f2;
    --white:#fff;
    --star:#f5b82e;
    --press:#707070;
  }
  *{box-sizing:border-box;margin:0;padding:0}
  html,body{width:1200px;height:915px;overflow:hidden}
  body{font-family:"Poppins",sans-serif;background:var(--white);color:var(--text);position:relative}
  .hero{position:absolute;left:0;top:0;width:1200px;height:718px;
    background:radial-gradient(circle at 230px 280px,#f6e9ea 0,rgba(246,233,234,0) 260px),var(--hero-bg)}
  .brand{position:absolute;left:158px;top:48px;display:flex;align-items:center;gap:9px;
    font-weight:600;font-size:32px;color:var(--teal);letter-spacing:-.5px}
  .brand-dot{width:30px;height:30px;border-radius:50%;background:var(--teal);opacity:.85}
  .nav{position:absolute;left:395px;top:58px;font-size:14px;color:var(--ink)}
  .nav a{color:inherit;text-decoration:none;display:flex;align-items:center;gap:5px;position:absolute;white-space:nowrap}
  .nav a.active{color:var(--teal)}
  .nav svg{width:10px;height:10px}
  .login{position:absolute;left:873px;top:58px;font-size:15px;font-weight:500;color:var(--teal)}
  .signup{position:absolute;left:944px;top:45px;width:104px;height:46px;border:1.5px solid var(--teal);
    border-radius:9px;color:var(--teal);font-size:15px;font-weight:500;display:flex;align-items:center;justify-content:center}
  .headline{position:absolute;left:151px;top:178px;width:560px;font-size:49px;font-weight:700;
    line-height:58px;color:var(--ink);letter-spacing:-1.2px;white-space:nowrap}
  .lead{position:absolute;left:152px;top:373px;width:500px;font-size:17px;line-height:27px;color:var(--ink)}
  .download{position:absolute;left:152px;top:460px;width:196px;height:46px;border-radius:8px;
    background:var(--teal);color:var(--white);font-size:16.5px;display:flex;align-items:center;justify-content:center;gap:9px}
  .rating{position:absolute;left:155px;top:525px;display:flex;align-items:center;font-size:14px;color:var(--muted)}
  .rating .score{font-size:15px;color:var(--ink);margin-right:10px}
  .stars{display:flex;gap:8px;margin-right:13px}
  .stars svg{width:11px;height:11px;fill:var(--star)}
  .avatars{position:absolute;left:150px;top:598px;width:100px;height:38px}
  .avatar{position:absolute;top:0;width:38px;height:38px;border-radius:50%;border:2px solid var(--white)}
  .proof{position:absolute;left:268px;top:606px;font-size:15.5px;color:var(--muted)}
  .proof b{font-weight:500;color:var(--ink)}
  .mark-3d{position:absolute;left:880px;top:242px;width:170px;height:312px;border-radius:48px;
    background:linear-gradient(150deg,#2de0c6,#12b49d 70%,#0e9c88);transform:skewY(4deg)}
  .phone{position:absolute;left:706px;top:196px;width:190px;height:393px;border-radius:32px;
    background:#e3e4e6;border:1px solid #c9cacc;padding:6px}
  .screen{position:relative;width:100%;height:100%;border-radius:27px;background:var(--white);overflow:hidden}
  .screen-head{height:74px;background:var(--teal);color:var(--white);padding:8px 14px 0}
  .status{font-size:6.5px;display:flex;justify-content:space-between}
  .notch{position:absolute;left:55px;top:0;width:68px;height:15px;background:#e3e4e6;border-radius:0 0 10px 10px}
  .greet{margin-top:20px;font-size:13px;font-weight:600}
  .user{position:absolute;right:12px;top:40px;width:20px;height:20px;border-radius:50%;background:var(--white)}
  .tabs{display:flex;font-size:6px;color:#777;border-bottom:1px solid #eee}
  .tabs span{flex:1;text-align:center;padding:8px 0 6px}
  .tabs span:first-child{border-bottom:1.5px solid var(--teal)}
  .tabs span:last-child{color:var(--teal)}
  .pick{font-size:6px;color:#444;padding:13px 17px}
  .year{margin:0 9px;height:42px;border-radius:6px;background:var(--teal);display:flex;align-items:center;
    padding:0 7px 0 18px;color:var(--white);font-size:14px;justify-content:space-between}
  .year span:last-child{background:var(--white);color:var(--teal);font-size:8px;font-weight:600;
    width:85px;height:27px;border-radius:5px;display:flex;align-items:center;justify-content:center}
  .home-bar{position:absolute;left:60px;bottom:9px;width:62px;height:2px;background:#222;border-radius:2px}
  .balance{position:absolute;left:673px;top:395px;width:254px;height:121px;border-radius:15px;
    background:rgba(255,255,255,.93);box-shadow:0 8px 30px rgba(0,0,0,.08);padding:16px 17px}
  .balance-top{display:flex;justify-content:space-between;font-size:10.5px;color:var(--ink)}
  .balance-icons{display:flex;gap:12px;align-items:center;font-size:12px;letter-spacing:1px}
  .amount{margin-top:6px;text-align:center;color:var(--ink);font-weight:500;font-size:27px}
  .amount sup{font-size:12px;font-weight:400;vertical-align:12px;margin-left:10px}
  .amount small{font-size:13px;vertical-align:8px;margin-right:6px}
  .refund{margin:6px auto 0;width:84px;height:24px;border:1px solid var(--teal);border-radius:12px;
    font-size:8px;color:var(--teal);display:flex;align-items:center;justify-content:center}
  .known{position:absolute;left:0;top:754px;width:1200px;text-align:center;font-size:17px;font-weight:500;color:var(--ink)}
  .known span{color:var(--teal)}
  .press{position:absolute;top:830px;transform:translateX(-50%);font-family:"Poppins",sans-serif;
    font-size:21px;font-weight:600;color:var(--press);white-space:nowrap}
</style>
</head>
<body>
<section class="hero">
  <div class="brand"><span class="brand-dot"></span>rendolo</div>
  <nav class="nav">
    <a class="active" style="left:0;top:0">Home <svg viewBox="0 0 10 10"><path d="M2 3.5l3 3 3-3" fill="none" stroke="currentColor" stroke-width="1.3"/></svg></a>
    <a style="left:79px;top:0">About us</a>
    <a style="left:160px;top:0">Services <svg viewBox="0 0 10 10"><path d="M2 3.5l3 3 3-3" fill="none" stroke="currentColor" stroke-width="1.3"/></svg></a>
    <a style="left:254px;top:0">Blog <svg viewBox="0 0 10 10"><path d="M2 3.5l3 3 3-3" fill="none" stroke="currentColor" stroke-width="1.3"/></svg></a>
    <a style="left:318px;top:0">Contact us</a>
  </nav>
  <div class="login">Login</div>
  <div class="signup">Sign up</div>

  <h1 class="headline">THE tool for getting<br>back your tax<br>money</h1>
  <p class="lead">Rendolo allows you to file tax easy, in only a few minutes and most importantly without any prior knowledge</p>
  <div class="download">
    <svg width="20" height="18" viewBox="0 0 20 18" fill="none" stroke="#fff" stroke-width="1.6" stroke-linecap="round"><path d="M10 2v9M6.5 7.5L10 11l3.5-3.5M2 11v3.5h16V11"/></svg>
    Download App
  </div>
  <div class="rating">
    <span class="score">4.8</span>
    <span class="stars">
      <svg viewBox="0 0 10 10"><path d="M5 0l1.5 3.2 3.5.4-2.6 2.4.7 3.5L5 7.8 1.9 9.5l.7-3.5L0 3.6l3.5-.4z"/></svg>
      <svg viewBox="0 0 10 10"><path d="M5 0l1.5 3.2 3.5.4-2.6 2.4.7 3.5L5 7.8 1.9 9.5l.7-3.5L0 3.6l3.5-.4z"/></svg>
      <svg viewBox="0 0 10 10"><path d="M5 0l1.5 3.2 3.5.4-2.6 2.4.7 3.5L5 7.8 1.9 9.5l.7-3.5L0 3.6l3.5-.4z"/></svg>
      <svg viewBox="0 0 10 10"><path d="M5 0l1.5 3.2 3.5.4-2.6 2.4.7 3.5L5 7.8 1.9 9.5l.7-3.5L0 3.6l3.5-.4z"/></svg>
      <svg viewBox="0 0 10 10"><path d="M5 0l1.5 3.2 3.5.4-2.6 2.4.7 3.5L5 7.8 1.9 9.5l.7-3.5L0 3.6l3.5-.4z"/></svg>
    </span>
    on 10k+ reviews
  </div>
  <div class="avatars">
    <div class="avatar" role="img" aria-label="Customer portrait" style="left:0;background:linear-gradient(135deg,#f08a8a,#7a4a3a)"></div>
    <div class="avatar" role="img" aria-label="Customer portrait" style="left:31px;background:linear-gradient(135deg,#f2a56a,#b24a3a)"></div>
    <div class="avatar" role="img" aria-label="Customer portrait" style="left:62px;background:linear-gradient(135deg,#f4c95a,#4a3022)"></div>
  </div>
  <div class="proof"><b>50k+</b> employee assessments</div>

  <div class="mark-3d" role="img" aria-label="3D brand block in teal beside the phone"></div>
  <div class="phone">
    <div class="screen">
      <div class="notch"></div>
      <div class="screen-head">
        <div class="status"><span>22:45</span><span>•••</span></div>
        <div class="greet">Hi, Mira!</div>
        <div class="user"></div>
      </div>
      <div class="tabs"><span>Steuerjahre</span><span>Statistik</span></div>
      <div class="pick">Wähle dein Steuerjahr</div>
      <div class="year"><span>2022</span><span>starten</span></div>
      <div class="home-bar"></div>
    </div>
  </div>
  <div class="balance">
    <div class="balance-top"><span>Balance</span>
      <span class="balance-icons">
        <svg width="11" height="12" viewBox="0 0 11 12" fill="none" stroke="#333" stroke-width="1"><path d="M2 8.5V5a3.5 3.5 0 017 0v3.5l1 1H1zM4.5 11h2"/></svg>···
      </span>
    </div>
    <div class="amount"><small>€</small>10,000<sup>.00</sup></div>
    <div class="refund">Refund Now</div>
  </div>
</section>

<h2 class="known">Known <span>from</span></h2>
<div class="press" style="left:218px">Vorbach</div>
<div class="press" style="left:408px">kurve</div>
<div class="press" style="left:598px">Orbita</div>
<div class="press" style="left:790px">geldwelt</div>
<div class="press" style="left:978px">Kapita</div>
</body>
</html>
```